Infectious Diseases Research Laboratory Needs Business Card

We need a business card for an academic research laboratory based in Kansas City called VELKOR. The full lab name is Microbe Exposure Kinetics/Response Modeling Integrated Study Laboratory, but this does not need to be incorporated. We study novel ways to optimize the treatment of multidrug-resistant bacterial infections ("superbugs") throughout the entire biomedical research spectrum (from benchtop to bedside). The name VELKOR is not only an acronym for our lab name, but also represents our desire to make discoveries and explore the unknown (the stars, if you well). It also serves as an ode to the state of Kansas motto where we are based, ad astra per aspera ("to the stars, through difficulty").

Target Market(s)

Pharmaceutical companies, researchers

Industry/Entity Type

Pharmaceutical

Contact Information for Business Card

The business card should incorporate and complement our new logo (see uploaded files). Double-sided designs are preferred. Looking for something modern, but professional.

Font styles to use
Sans Serif

Requirements
Must have
• Double-sided. One side would ideally be a solid color incorporating logo and the other should also have the logo (smaller), but incorporate staff information.
• Color codes:
• Red: #F04C51
• Blue: #3477B5
• Gray: #808285

```html
<!DOCTYPE html>
<html lang="en">
<head>
<meta charset="utf-8">
<title>VELKOR Business Card</title>
<link href="https://fonts.googleapis.com/css2?family=Roboto:wght@400;500;700&display=swap" rel="stylesheet">
<style>
  :root {
    --red: #F04C51;
    --blue: #3477B5;
    --gray: #808285;
    --ink: #1e1e1e;
    --white: #ffffff;
    --backdrop: #2b2b2b;
  }
  * { margin: 0; padding: 0; box-sizing: border-box; }
  html, body { width: 1200px; height: 900px; overflow: hidden; }
  body {
    background: var(--backdrop);
    font-family: "Roboto", Arial, sans-serif;
    position: relative;
  }
  .card {
    position: absolute;
    left: 260px;
    width: 680px;
    height: 389px;
    border-radius: 22px;
    overflow: hidden;
  }
  .card--front { top: 40px; background: var(--red); }
  .card--back { top: 471px; background: var(--white); }

  /* Front */
  .front-brand {
    position: absolute;
    left: 0; right: 0; top: 140px;
    display: flex; align-items: center; justify-content: center; gap: 22px;
  }
  .front-brand__dot {
    width: 64px; height: 64px; border-radius: 50%;
    background: var(--white);
  }
  .front-brand__name {
    color: var(--white);
    font-weight: 500;
    font-size: 92px;
    letter-spacing: 6px;
    line-height: 1;
  }
  .front-web {
    position: absolute;
    left: 0; right: 0; bottom: 36px;
    text-align: center;
    color: var(--white);
    font-size: 17px;
    letter-spacing: 0.5px;
  }

  /* Back */
  .back-brand {
    position: absolute; left: 42px; top: 44px;
    display: flex; align-items: center; gap: 14px;
  }
  .back-brand__dot {
    width: 40px; height: 40px; border-radius: 50%;
    background: var(--red);
  }
  .back-brand__name {
    color: var(--red);
    font-weight: 500;
    font-size: 50px;
    letter-spacing: 4px;
    line-height: 1;
  }
  .back-brand__sub {
    position: absolute; left: 96px; top: 104px;
    width: 290px;
    color: var(--gray);
    font-size: 8px;
    letter-spacing: 0.8px;
    text-transform: uppercase;
    line-height: 1.45;
    border-top: 1px solid var(--gray);
    padding-top: 4px;
  }
  .person {
    position: absolute; left: 42px; top: 186px;
  }
  .person__name {
    color: var(--red);
    font-weight: 700;
    font-size: 30px;
  }
  .person__role {
    color: var(--ink);
    font-size: 17px;
    margin-top: 2px;
  }
  .address {
    position: absolute; right: 42px; top: 200px;
    text-align: right;
    color: var(--ink);
    font-size: 16px;
    line-height: 1.4;
  }
  .divider {
    position: absolute; left: 42px; right: 42px; top: 262px;
    height: 3px; background: var(--blue);
  }
  .contacts {
    position: absolute; left: 42px; top: 278px;
    list-style: none;
  }
  .contacts__item {
    display: flex; align-items: center; gap: 12px;
    color: var(--ink);
    font-size: 17px;
    line-height: 1.7;
  }
  .contacts__icon { width: 16px; height: 16px; flex: none; }
</style>
</head>
<body>

<section class="card card--front" aria-label="Card front">
  <div class="front-brand">
    <span class="front-brand__dot"></span>
    <span class="front-brand__name">VELKOR</span>
  </div>
  <p class="front-web">www.velkorlab.org</p>
</section>

<section class="card card--back" aria-label="Card back">
  <div class="back-brand">
    <span class="back-brand__dot"></span>
    <span class="back-brand__name">VELKOR</span>
  </div>
  <p class="back-brand__sub">Microbe Exposure Kinetics/Response Modeling Integrated Study Laboratory</p>

  <div class="person">
    <p class="person__name">Marlow Pennick</p>
    <p class="person__role">Owner</p>
  </div>

  <p class="address">2410 Grand Blvd, Suite 7,<br>Kansas City, MO 64108</p>

  <div class="divider"></div>

  <ul class="contacts">
    <li class="contacts__item">
      <svg class="contacts__icon" viewBox="0 0 24 24" aria-hidden="true"><path fill="#F04C51" d="M6.6 10.8a15.1 15.1 0 0 0 6.6 6.6l2.2-2.2c.3-.3.7-.4 1-.2 1.1.4 2.3.6 3.6.6.6 0 1 .4 1 1V20c0 .6-.4 1-1 1A17 17 0 0 1 3 4c0-.6.4-1 1-1h3.5c.6 0 1 .4 1 1 0 1.3.2 2.5.6 3.6.1.3 0 .7-.2 1z"/></svg>
      816-555-0148
    </li>
    <li class="contacts__item">
      <svg class="contacts__icon" viewBox="0 0 24 24" aria-hidden="true"><rect x="2" y="5" width="20" height="14" rx="1.5" fill="#F04C51"/><path d="M3 6l9 7 9-7" fill="none" stroke="#fff" stroke-width="1.6"/></svg>
      mpennick@velkorlab.org
    </li>
    <li class="contacts__item">
      <svg class="contacts__icon" viewBox="0 0 24 24" aria-hidden="true"><circle cx="12" cy="12" r="10" fill="#F04C51"/><path d="M2 12h20M12 2c3 3 3 17 0 20M12 2c-3 3-3 17 0 20" fill="none" stroke="#fff" stroke-width="1.4"/></svg>
      www.velkorlab.org
    </li>
  </ul>
</section>

</body>
</html>
```